Veltra Homes Real Estate Brokerage Recruiting Flyer

We are a real estate brokerage looking to hire more real estate agents. We need to list everything we have to offer as a company so real estate agents will join our company. this is our company website: www.Veltrahomes.example .

100% COMMISSION NO MONTHLY FEE
$450 Flat Transaction FEE

What We Offer:
24/7 Office Access
Free E & O Insurance for 1st Year
Free Online CE and PLE
Free 1,000 Business Cards
Free Professional Social Media Marketing
Free Printing, Scanning, and Copies
Free Buyer and Seller Presentation Packages
Free Papervane Cloud Based Document Management Access
Access to our Internal Brokerage Forum
Company Profit Sharing!
Private Offices Available to Rent

*Lead Generation Software with over 3,000 Leads
*10 Leads to Start
* Free Personal CRM and Website
*Restrictions and Rules apply

Company Address:
4817 Marlow Creek Road
Suite 412
Fairfax, VA 22147
Phone: 703-241-7086
email: info@veltrahomes.example

Target Market(s)

Real Estate Agents

Industry/Entity Type

Real Estate

Colors
0555a3
ffffff

Requirements
Must have
• 100% COMMISSION NO MONTHLY FEE
$450 Flat Transaction FEE

What We Offer:
24/7 Office Access
Free Online CE and PLE
Free 1,000 Business Cards
Company Profit Sharing!

*10 Leads to Start

Company Address:
4817 Marlow Creek Road
Suite 412
Fairfax, VA 22147
Phone: 703-241-7086

```html
<!DOCTYPE html>
<html lang="en">
<head>
<meta charset="utf-8">
<title>Veltra Homes – Agent Recruiting Flyer</title>
<link rel="stylesheet" href="https://fonts.googleapis.com/css2?family=Oswald:wght@500;700&family=Lato:wght@400;700&display=swap">
<style>
  :root {
    --navy: #0a3470;
    --brand-blue: #0555a3;
    --panel-grey: #d2d3d5;
    --ink: #333436;
    --text: #1f2328;
    --white: #ffffff;
    --stage: #ececec;
  }
  * { box-sizing: border-box; margin: 0; padding: 0; }
  html, body { width: 1200px; height: 1200px; overflow: hidden; background: var(--stage); }
  body { font-family: 'Lato', sans-serif; color: var(--text); }

  .flyer {
    position: absolute; left: 193px; top: 30px;
    width: 813px; height: 1140px;
    background: var(--white);
    box-shadow: 0 6px 24px rgba(0,0,0,.18);
    overflow: hidden;
  }

  .hero-photo {
    position: absolute; left: 0; top: 0; width: 813px; height: 382px;
    background: linear-gradient(160deg, #6f8a3a 0%, #8fa84a 35%, #c9a64a 70%, #e59a2c 100%);
  }

  .gallery {
    position: absolute; left: 43px; top: 322px; width: 727px; height: 148px;
    background: var(--white); padding: 8px 9px;
    display: flex; gap: 9px;
  }
  .gallery-photo { flex: 1; height: 100%; }
  .gallery-photo.exterior { background: linear-gradient(180deg, #5f7a4a 0%, #8a6a55 55%, #b7aea2 100%); }
  .gallery-photo.kitchen  { background: linear-gradient(180deg, #e8e8e6 0%, #c9c8c4 55%, #8d7f6d 100%); }
  .gallery-photo.living   { background: linear-gradient(180deg, #9a8fb0 0%, #b8a98c 55%, #5c4334 100%); }

  .gallery-shadow {
    position: absolute; left: 60px; top: 472px; width: 693px; height: 10px;
    background: radial-gradient(ellipse at center top, rgba(0,0,0,.28), rgba(0,0,0,0) 70%);
  }

  .headline-sub {
    position: absolute; left: 0; top: 484px; width: 813px; text-align: center;
    font-family: 'Oswald', sans-serif; font-weight: 500; font-size: 40px; line-height: 48px;
    color: var(--ink); letter-spacing: .5px;
  }
  .headline-main {
    position: absolute; left: 0; top: 528px; width: 813px; text-align: center;
    font-family: 'Oswald', sans-serif; font-weight: 700; font-size: 66px; line-height: 76px;
    color: var(--navy); letter-spacing: -0.5px;
  }

  .offer-panel { position: absolute; top: 611px; height: 395px; }
  .offer-panel.perks { left: 0; width: 420px; background: var(--navy); color: var(--white); padding: 20px 0 0 31px; }
  .offer-panel.leads { left: 420px; width: 393px; background: var(--panel-grey); padding: 20px 0 0 26px; }

  .panel-title {
    font-family: 'Oswald', sans-serif; font-weight: 500; font-size: 24px; line-height: 30px; letter-spacing: .3px;
  }
  .perks .panel-title { color: var(--white); }
  .leads .panel-title { color: var(--navy); }

  .title-rule { position: relative; height: 2px; width: 322px; margin-top: 12px; }
  .perks .title-rule { background: rgba(255,255,255,.85); }
  .perks .title-rule::before { content: ""; position: absolute; left: 0; top: -1px; width: 178px; height: 4px; background: var(--white); }
  .leads .title-rule { background: var(--navy); }
  .leads .title-rule::before { content: ""; position: absolute; left: 0; top: -1px; width: 178px; height: 4px; background: var(--navy); }

  .perk-list { list-style: none; margin-top: 23px; }
  .perk-list li {
    display: flex; align-items: center; gap: 9px;
    font-size: 13px; line-height: 26.6px; color: var(--white);
  }
  .perk-list svg { width: 15px; height: 15px; flex: none; }

  .lead-list { list-style: none; margin-top: 16px; }
  .lead-list li { display: flex; align-items: center; gap: 17px; height: 79px; font-size: 15px; line-height: 19px; color: var(--text); }
  .lead-icon {
    width: 55px; height: 55px; border-radius: 50%; background: var(--navy); flex: none;
    display: flex; align-items: center; justify-content: center;
  }
  .lead-icon svg { width: 32px; height: 32px; }

  .contact { position: absolute; left: 28px; top: 1022px; }
  .contact-phone { display: flex; align-items: center; gap: 6px; font-size: 23px; font-weight: 700; color: var(--text); line-height: 30px; }
  .contact-line { display: flex; align-items: center; gap: 6px; font-size: 15px; line-height: 23px; margin-top: 2px; }
  .contact svg { flex: none; }

  .brand-name {
    position: absolute; left: 283px; top: 1050px; width: 260px; text-align: center;
    font-family: 'Lato', sans-serif; font-weight: 700; font-size: 34px; line-height: 40px; color: var(--navy);
  }

  .address { position: absolute; right: 30px; top: 1030px; text-align: right; font-size: 15px; line-height: 20px; }
  .address-pin { position: absolute; right: -20px; top: 0; }
</style>
</head>
<body>
<main class="flyer">
  <div class="hero-photo" role="img" aria-label="Happy family sitting on a lawn holding a paper roof over their heads"></div>

  <div class="gallery">
    <div class="gallery-photo exterior" role="img" aria-label="Brick townhouse exterior with trees"></div>
    <div class="gallery-photo kitchen" role="img" aria-label="Bright modern kitchen with island and stools"></div>
    <div class="gallery-photo living" role="img" aria-label="Open living room and kitchen interior"></div>
  </div>
  <div class="gallery-shadow"></div>

  <h2 class="headline-sub">100% COMMISSION NO MONTHLY FEE</h2>
  <h1 class="headline-main">$450 FLAT TRANSACTION FEE</h1>

  <section class="offer-panel perks">
    <h3 class="panel-title">WHAT WE OFFER:</h3>
    <div class="title-rule"></div>
    <ul class="perk-list">
      <li><svg viewBox="0 0 16 16"><circle cx="8" cy="8" r="6.5" fill="none" stroke="#fff" stroke-width="1.4"/><path d="M5 8.2l2.2 2.2L13.5 3.5" fill="none" stroke="#fff" stroke-width="1.6"/></svg>24/7 Office Access</li>
      <li><svg viewBox="0 0 16 16"><circle cx="8" cy="8" r="6.5" fill="none" stroke="#fff" stroke-width="1.4"/><path d="M5 8.2l2.2 2.2L13.5 3.5" fill="none" stroke="#fff" stroke-width="1.6"/></svg>Free E &amp; O Insurance for 1st Year</li>
      <li><svg viewBox="0 0 16 16"><circle cx="8" cy="8" r="6.5" fill="none" stroke="#fff" stroke-width="1.4"/><path d="M5 8.2l2.2 2.2L13.5 3.5" fill="none" stroke="#fff" stroke-width="1.6"/></svg>Free Online CE and PLE</li>
      <li><svg viewBox="0 0 16 16"><circle cx="8" cy="8" r="6.5" fill="none" stroke="#fff" stroke-width="1.4"/><path d="M5 8.2l2.2 2.2L13.5 3.5" fill="none" stroke="#fff" stroke-width="1.6"/></svg>Free 1,000 Business Cards</li>
      <li><svg viewBox="0 0 16 16"><circle cx="8" cy="8" r="6.5" fill="none" stroke="#fff" stroke-width="1.4"/><path d="M5 8.2l2.2 2.2L13.5 3.5" fill="none" stroke="#fff" stroke-width="1.6"/></svg>Free Professional Social Media Marketing</li>
      <li><svg viewBox="0 0 16 16"><circle cx="8" cy="8" r="6.5" fill="none" stroke="#fff" stroke-width="1.4"/><path d="M5 8.2l2.2 2.2L13.5 3.5" fill="none" stroke="#fff" stroke-width="1.6"/></svg>Free Printing, Scanning, and Copies</li>
      <li><svg viewBox="0 0 16 16"><circle cx="8" cy="8" r="6.5" fill="none" stroke="#fff" stroke-width="1.4"/><path d="M5 8.2l2.2 2.2L13.5 3.5" fill="none" stroke="#fff" stroke-width="1.6"/></svg>Free Buyer and Seller Presentation Packages</li>
      <li><svg viewBox="0 0 16 16"><circle cx="8" cy="8" r="6.5" fill="none" stroke="#fff" stroke-width="1.4"/><path d="M5 8.2l2.2 2.2L13.5 3.5" fill="none" stroke="#fff" stroke-width="1.6"/></svg>Free Papervane Cloud Based Document Management Access</li>
      <li><svg viewBox="0 0 16 16"><circle cx="8" cy="8" r="6.5" fill="none" stroke="#fff" stroke-width="1.4"/><path d="M5 8.2l2.2 2.2L13.5 3.5" fill="none" stroke="#fff" stroke-width="1.6"/></svg>Access to our Internal Brokerage Forum</li>
      <li><svg viewBox="0 0 16 16"><circle cx="8" cy="8" r="6.5" fill="none" stroke="#fff" stroke-width="1.4"/><path d="M5 8.2l2.2 2.2L13.5 3.5" fill="none" stroke="#fff" stroke-width="1.6"/></svg>Company Profit Sharing!</li>
      <li><svg viewBox="0 0 16 16"><circle cx="8" cy="8" r="6.5" fill="none" stroke="#fff" stroke-width="1.4"/><path d="M5 8.2l2.2 2.2L13.5 3.5" fill="none" stroke="#fff" stroke-width="1.6"/></svg>Private Offices Available to Rent</li>
    </ul>
  </section>

  <section class="offer-panel leads">
    <h3 class="panel-title">WHAT WE OFFER:</h3>
    <div class="title-rule"></div>
    <ul class="lead-list">
      <li>
        <span class="lead-icon"><svg viewBox="0 0 32 32" fill="none" stroke="#fff" stroke-width="1.8"><circle cx="16" cy="15" r="4.5"/><path d="M16 4v4M16 22v4M5 15h4M23 15h4M8.2 7.2l2.8 2.8M21 20l2.8 2.8M8.2 22.8L11 20M21 10l2.8-2.8"/><path d="M11 27l3 2 6-6"/></svg></span>
        <span>Lead Generation Software with over<br>3,000 Leads</span>
      </li>
      <li>
        <span class="lead-icon"><svg viewBox="0 0 32 32" fill="#fff"><circle cx="16" cy="9" r="4"/><path d="M7 27c0-6 4-10 9-10s9 4 9 10z"/></svg></span>
        <span>10 Leads to Start</span>
      </li>
      <li>
        <span class="lead-icon"><svg viewBox="0 0 32 32" fill="none" stroke="#fff" stroke-width="1.8"><rect x="5" y="6" width="22" height="20" rx="1.5"/><path d="M5 11h22M11 19l3 3 7-7"/></svg></span>
        <span>Free Personal CRM and Website</span>
      </li>
      <li>
        <span class="lead-icon"><svg viewBox="0 0 32 32" fill="none" stroke="#fff" stroke-width="1.8"><path d="M20 27H8V5h11l4 4v8"/><path d="M11 11h8M11 15h8M11 19h5"/><circle cx="23" cy="23" r="4.5"/><path d="M21 23l1.6 1.6 2.8-3"/></svg></span>
        <span>Restrictions and Rules apply</span>
      </li>
    </ul>
  </section>

  <footer>
    <div class="contact">
      <div class="contact-phone"><svg width="14" height="24" viewBox="0 0 14 24"><path d="M10 2L5 3C2 8 2 16 5 21l5 1 1-5-3-1c-1-3-1-6 0-8l3-1z" fill="#1f2328"/></svg>703-241-7086</div>
      <div class="contact-line"><svg width="20" height="14" viewBox="0 0 20 14"><rect x="1" y="1" width="18" height="12" fill="none" stroke="#0a3470" stroke-width="1.6"/><path d="M1 1l9 7 9-7" fill="none" stroke="#0a3470" stroke-width="1.6"/></svg>info@veltrahomes.example</div>
      <div class="contact-line"><svg width="18" height="18" viewBox="0 0 18 18" fill="none" stroke="#0a3470" stroke-width="1.5"><circle cx="9" cy="9" r="7.5"/><ellipse cx="9" cy="9" rx="3.3" ry="7.5"/><path d="M1.5 9h15M3 5h12M3 13h12"/></svg>www.Veltrahomes.example</div>
    </div>

    <div class="brand-name">Veltra Homes</div>

    <address class="address" style="font-style:normal">
      4817 Marlow Creek Road<br>Suite 412<br>Fairfax, VA 22147
      <svg class="address-pin" width="14" height="18" viewBox="0 0 14 18" fill="none" stroke="#0a3470" stroke-width="1.6"><path d="M7 12C4 8.5 2.5 6.5 2.5 5a4.5 4.5 0 019 0c0 1.5-1.5 3.5-4.5 7z"/><circle cx="7" cy="5" r="1.6"/><path d="M2 16h10"/></svg>
    </address>
  </footer>
</main>
</body>
</html>
```